Painting business fun and professional website

Looking for a website design that is easy to navigate, attractive, energetic, and professional. Include categories/pages: About, Residential, Commercial, Etc.

Target Market(s)

Home owners, Property managers, builders, maintenance supervisors, etc.

Industry/Entity Type

painting, construction

Number of Pages Required

4 page

Other font styles liked:
• This font for categories, but not all the literature.Latino www.brantowtype.com/fonts/a-morvel

Colors
0094D4
00A9DD
6FCCEA
C7EBF8
E9F6FB
FFF300
FFF600
FEFA6F
FFFEC7
FFFEE8
EB3D1F
EC4F4E
F09395
F8D3D4
FCEDEE

Requirements
Must have
• Connect with social media handles, short transformation videos, photos, Quick Quote request. Colors Red (R247 G32 B0 #f72300 C0 M98 Y93 K0), Blue (R0, G204, B255 #00CCFF C65 M0 Y0 K0) Yellow (R255, G255, B0 #FFE100 C2 M7 Y100 K0)
Nice to have
• Website design to stand out from other painting business websites in a fun and modern way. Nothing stale, boring, or basic please

```html
<!DOCTYPE html>
<html lang="en">
<head>
<meta charset="utf-8">
<title>Brightcoat Painting</title>
<link rel="stylesheet" href="https://fonts.googleapis.com/css2?family=Alfa+Slab+One&family=Bangers&family=Oswald:wght@400;500;600&family=Open+Sans:ital,wght@0,400;0,600;1,400&family=Poppins:wght@400;500&display=swap">
<style>
:root{
  --blue:#00a9dd;
  --blue-deep:#0094d4;
  --blue-bright:#00bde8;
  --yellow:#ffe100;
  --red:#ec4f4e;
  --pink:#f09395;
  --amber:#f6b10f;
  --ink:#1c1c1c;
  --nav:#2b2b2b;
  --dark:#1d1d23;
  --darker:#141418;
  --line:#e4e4e4;
  --white:#ffffff;
}
*{box-sizing:border-box;margin:0;padding:0}
html,body{width:1200px;height:4476px;overflow:hidden}
body{position:relative;background:var(--white);font-family:"Open Sans",sans-serif;color:var(--ink)}
.abs{position:absolute}
.slab{font-family:"Alfa Slab One",serif;letter-spacing:3px;text-transform:uppercase;font-weight:400}

/* header */
.topline{top:12px;font-family:"Oswald",sans-serif;font-size:11px;color:#555;display:flex;align-items:center;gap:7px;letter-spacing:.3px}
.callbar{left:155px;top:53px;width:245px;height:41px;background:var(--yellow);border-radius:3px;display:flex;align-items:center;font-family:"Oswald",sans-serif;font-weight:500;font-size:16px;color:var(--ink)}
.callbar .lbl{padding:0 15px}
.callbar .num{border-left:2px solid #e0a800;padding-left:15px;height:100%;display:flex;align-items:center}
.brand{left:520px;top:14px;width:160px;height:80px;display:flex;align-items:center;justify-content:center;gap:8px}
.brand .dot{width:18px;height:18px;border-radius:50%;background:var(--yellow)}
.brand span{font-family:"Oswald",sans-serif;font-weight:600;font-size:22px;color:var(--blue);line-height:1;text-transform:uppercase;letter-spacing:.5px}
.search{left:760px;top:53px;width:290px;height:41px;background:var(--yellow);border-radius:3px;display:flex;align-items:center;justify-content:space-between;padding:0 14px 0 18px;font-family:"Oswald",sans-serif;font-size:14px;color:#c9a800;letter-spacing:.5px}
.nav{left:0;top:110px;width:1200px;height:50px;background:var(--nav);font-family:"Oswald",sans-serif;font-weight:500;font-size:13px;color:var(--white);letter-spacing:.3px}
.nav a{position:absolute;top:16px;color:var(--white);text-decoration:none}

/* hero */
.hero{left:0;top:160px;width:1200px;height:537px;overflow:hidden}
.hero-photo{position:absolute;inset:0;background:linear-gradient(180deg,#d9b84a 0%,#e0be48 55%,#c8c1b5 62%,#cfc7bb 75%,#b98d5e 78%,#c89c6e 100%)}
.hero-badge{position:absolute;left:150px;top:40px;width:460px;height:420px;border-radius:50%;background:radial-gradient(circle,var(--blue-bright) 0%,var(--blue-bright) 60%,#13a9d6 100%)}
.hero-text{position:absolute;left:150px;top:160px;width:460px;text-align:center;font-family:"Bangers",cursive;line-height:1}
.hero-text .small{font-size:40px;color:var(--white);letter-spacing:3px}
.hero-text .big{font-size:66px;color:var(--yellow);letter-spacing:4px;display:block;margin-top:2px}

/* section headings */
.h2{left:0;width:1200px;text-align:center;font-size:40px;line-height:48px;color:var(--ink)}
.lead{left:330px;width:540px;text-align:center;font-size:12.5px;line-height:23px;color:#333}

/* service cards */
.card{top:972px;width:226px;height:275px;color:var(--white);text-align:center}
.card svg.shape{position:absolute;inset:0}
.card .inner{position:relative;padding:60px 18px 0}
.card h3{font-family:"Poppins",sans-serif;font-weight:400;font-size:19px;line-height:23px;margin-top:6px}
.card p{font-size:11px;line-height:19px;margin-top:12px}

/* videos */
.videos{left:182px;top:1332px;width:846px;height:580px;background:var(--red)}
.video{position:absolute;overflow:hidden}
.play{position:absolute;border-radius:50%;background:var(--white);display:flex;align-items:center;justify-content:center}

/* gallery */
.photo{position:absolute}

/* quote */
.quote{left:0;top:2788px;width:1200px;height:477px;background:var(--blue);overflow:hidden}
.field{position:absolute;background:var(--white);border-radius:4px;font-size:11px;color:#888;padding:0 20px;display:flex;align-items:center}
.send{left:512px;top:3172px;width:176px;height:46px;background:var(--yellow);border-radius:3px;font-family:"Oswald",sans-serif;font-size:15px;font-weight:500;display:flex;align-items:center;justify-content:center;color:var(--ink)}

/* testimonials */
.tcard{position:absolute;width:272px;height:297px;background:var(--white);border:1px solid var(--line);padding:38px 20px 0}
.tcard.raised{box-shadow:0 8px 24px rgba(0,0,0,.08);border-color:#f0f0f0}
.stars{color:var(--amber);font-size:11px;letter-spacing:2px}
.tcard p{font-style:italic;font-size:12px;line-height:25px;color:#555;margin-top:22px}
.tcard p b{font-weight:400;color:var(--ink)}
.tcard .who{position:absolute;left:22px;bottom:28px;font-family:"Poppins",sans-serif;font-size:13px;color:var(--ink)}
.tcard .who small{display:block;font-size:10px;color:#999;font-family:"Open Sans",sans-serif}
.tcard.raised .who{color:var(--blue)}

/* footer */
.footer{left:0;top:3910px;width:1200px;height:566px;background:var(--dark);color:#9a9aa2}
.sub-title{left:0;top:3970px;width:1200px;text-align:center;font-size:20px;color:var(--yellow);letter-spacing:2px}
.sub-input{left:370px;top:4023px;width:335px;height:40px;background:#2a2a31;font-size:11px;color:#777;display:flex;align-items:center;padding-left:48px}
.sub-btn{left:704px;top:4023px;width:128px;height:40px;background:var(--yellow);font-family:"Oswald",sans-serif;font-weight:500;font-size:15px;color:var(--ink);display:flex;align-items:center;justify-content:center}
.tagline{left:0;top:4086px;width:1200px;text-align:center;font-family:"Oswald",sans-serif;font-size:13px;letter-spacing:3.5px;color:#c9c9cf}
.fcol{top:4200px;font-size:11px;line-height:26px;color:#8d8d96}
.fcol h4{font-family:"Oswald",sans-serif;font-weight:500;font-size:13px;color:var(--white);letter-spacing:.5px;margin-bottom:10px}
.bottombar{left:0;top:4410px;width:1200px;height:66px;background:var(--darker);font-size:10px;color:#cfcfd4}
.soc{position:absolute;top:24px;width:20px;height:20px;border-radius:50%;background:#2c2c34}
</style>
</head>
<body>

<!-- header -->
<div class="abs topline" style="left:155px">
  <svg width="16" height="11" viewBox="0 0 16 11"><rect x=".5" y=".5" width="15" height="10" fill="none" stroke="#777"/><path d="M.5 .5l7.5 6 7.5-6" fill="none" stroke="#777"/></svg>
  EMAIL US : HELLO@BRIGHTCOATPAINT.COM
</div>
<div class="abs topline" style="left:780px">
  <svg width="12" height="15" viewBox="0 0 12 15"><path d="M6 14s5-5 5-8.5A5 5 0 0 0 1 5.5C1 9 6 14 6 14z" fill="none" stroke="#777"/><circle cx="6" cy="5.5" r="1.8" fill="none" stroke="#777"/></svg>
  FIND US : 240 MAPLE ROW, SPRINGFIELD
</div>
<div class="abs callbar"><span class="lbl">CALL US</span><span class="num">05 55 01 23 45</span></div>
<div class="abs brand"><i class="dot"></i><span>Brightcoat<br>Painting</span></div>
<div class="abs search">SEARCH
  <svg width="16" height="16" viewBox="0 0 16 16"><circle cx="7" cy="7" r="5.5" fill="none" stroke="#333" stroke-width="1.4"/><path d="M11 11l4 4" stroke="#333" stroke-width="1.4"/></svg>
</div>
<nav class="abs nav">
  <a style="left:168px">HOME</a>
  <a style="left:266px">ABOUT</a>
  <a style="left:370px">RESIDENTIAL</a>
  <a style="left:508px">COMMERCIAL</a>
  <a style="left:654px">BEFORE/AFTER VIDEOS</a>
  <a style="left:852px">CONTACT US</a>
  <a style="left:969px">|</a>
  <a style="left:1008px">EN ▾</a>
</nav>

<!-- hero -->
<section class="abs hero">
  <div class="hero-photo" role="img" aria-label="Freshly painted living room with mustard wall, grey armchair, shelves and plants"></div>
  <div class="hero-badge" role="img" aria-label="Bright blue comic burst badge behind the headline"></div>
  <div class="hero-text"><span class="small">YOUR ONE STOP</span><span class="big">PAINTING<br>SOLUTIONS</span></div>
</section>

<!-- solutions -->
<h2 class="abs h2 slab" style="top:782px">Solutions for<br>your painting needs</h2>
<p class="abs lead" style="top:894px">Nam mollis sollicitudin eleifend. Proin varius erat in ex pretium consectetur. Vivamus egestas suscipit odio, sed sodales nunc interdum nec.</p>

<div class="abs card" style="left:112px">
  <svg class="shape" viewBox="0 0 226 275" preserveAspectRatio="none"><polygon fill="var(--blue)" points="0,4 20,12 40,2 62,14 90,6 120,16 150,4 180,14 205,6 226,10 226,275 113,255 0,275"/></svg>
  <div class="inner">
    <svg width="40" height="40" viewBox="0 0 40 40" fill="none" stroke="#fff" stroke-width="1.6"><path d="M6 34L26 14M28 6a6 6 0 1 0 6 6l-4 1-3-3z"/><path d="M6 6l5 0 20 20 3 8-8-3L6 11z"/></svg>
    <h3>Repair and<br>maintenance</h3>
    <p>Nam mollis sollicitudin eleifend varius erat in ex pretium consect Vivamus egestas</p>
  </div>
</div>
<div class="abs card" style="left:360px">
  <svg class="shape" viewBox="0 0 226 275" preserveAspectRatio="none"><polygon fill="var(--pink)" points="0,2 25,14 50,4 80,16 105,6 135,14 160,2 190,16 210,4 226,12 226,275 113,255 0,275"/></svg>
  <div class="inner">
    <svg width="40" height="40" viewBox="0 0 40 40" fill="none" stroke="#fff" stroke-width="1.6"><rect x="8" y="20" width="24" height="12"/><path d="M12 20v-6h16v6M6 32h28M12 14V6h16v8"/></svg>
    <h3>Decoration<br>visualization</h3>
    <p>Nam mollis sollicitudin eleifend varius erat in ex pretium consect Vivamus egestas</p>
  </div>
</div>
<div class="abs card" style="left:608px">
  <svg class="shape" viewBox="0 0 226 275" preserveAspectRatio="none"><polygon fill="var(--amber)" points="0,8 22,2 48,14 74,4 100,12 128,2 156,14 182,4 206,14 226,6 226,275 113,255 0,275"/></svg>
  <div class="inner">
    <svg width="40" height="40" viewBox="0 0 40 40" fill="none" stroke="#fff" stroke-width="1.6"><path d="M4 20L20 6l16 14M8 17v17h24V17"/><rect x="16" y="24" width="8" height="10"/></svg>
    <h3>Residential<br>Painting</h3>
    <p>Nam mollis sollicitudin eleifend varius erat in ex pretium consect Vivamus egestas</p>
  </div>
</div>
<div class="abs card" style="left:856px">
  <svg class="shape" viewBox="0 0 226 275" preserveAspectRatio="none"><polygon fill="var(--red)" points="0,4 24,14 50,2 76,12 100,4 130,16 156,6 180,14 204,2 226,10 226,275 113,255 0,275"/></svg>
  <div class="inner">
    <svg width="40" height="40" viewBox="0 0 40 40" fill="none" stroke="#fff" stroke-width="1.6"><rect x="10" y="8" width="14" height="26"/><rect x="24" y="18" width="10" height="16"/><path d="M14 13h6M14 19h6M14 25h6M6 34h32"/></svg>
    <h3>Commercial<br>Painting</h3>
    <p>Nam mollis sollicitudin eleifend varius erat in ex pretium consect Vivamus egestas</p>
  </div>
</div>

<!-- short videos -->
<section class="abs videos">
  <h2 class="slab" style="position:absolute;left:0;top:70px;width:846px;text-align:center;font-size:38px;color:#fff;letter-spacing:4px">Short videos</h2>
</section>
<div class="video" style="left:33px;top:1590px;width:282px;height:210px;background:linear-gradient(160deg,#6f7a5a,#c9c6b6 50%,#3b4236)" role="img" aria-label="Video thumbnail: painter working on a house exterior">
  <span class="play" style="left:26px;top:130px;width:60px;height:60px"><svg width="18" height="20" viewBox="0 0 18 20"><path d="M2 1l15 9-15 9z" fill="#111"/></svg></span>
</div>
<div class="video" style="left:345px;top:1495px;width:520px;height:345px;background:linear-gradient(150deg,#8a8a4a,#b8b37a 40%,#6b3f23 75%,#a0623a);box-shadow:0 12px 30px rgba(0,0,0,.25)" role="img" aria-label="Video thumbnail: painted dining room with wooden table and chandelier">
  <span class="play" style="left:38px;top:245px;width:80px;height:80px"><svg width="24" height="28" viewBox="0 0 18 20"><path d="M2 1l15 9-15 9z" fill="#111"/></svg></span>
</div>
<div class="video" style="left:893px;top:1590px;width:283px;height:210px;background:linear-gradient(160deg,#4fa6ae,#7cc3c4 55%,#3a7f88)" role="img" aria-label="Video thumbnail: painter rolling teal paint on a wall">
  <span class="play" style="left:25px;top:128px;width:62px;height:62px"><svg width="18" height="20" viewBox="0 0 18 20"><path d="M2 1l15 9-15 9z" fill="#111"/></svg></span>
</div>

<!-- gallery -->
<h2 class="abs h2 slab" style="top:1998px">Solutions for<br>your painting needs</h2>
<div class="photo" style="left:156px;top:2133px;width:380px;height:280px;background:linear-gradient(160deg,#d89a2c,#e7b54d 45%,#b06c2a)" role="img" aria-label="Bright yellow painted interior room with chandelier and fireplace"></div>
<div class="photo" style="left:548px;top:2133px;width:494px;height:280px;background:linear-gradient(180deg,#4f8fd0,#a9c9e6 45%,#e6e4df 60%,#9a7a5a)" role="img" aria-label="New house exterior under painting with ladders and paint buckets"></div>
<div class="photo" style="left:156px;top:2423px;width:494px;height:280px;background:linear-gradient(90deg,#e4e2de 0%,#dcdad5 48%,#2d4a3e 50%,#243d33 100%)" role="img" aria-label="Modern living room with white and deep green walls, grey sofa and orange lamps"></div>
<div class="photo" style="left:662px;top:2423px;width:380px;height:280px;background:linear-gradient(160deg,#e9e4dc,#cdbfa9 55%,#6b4a34)" role="img" aria-label="Warm neutral living room with beige sofa, plants and wood panels"></div>

<!-- quick quote -->
<section class="abs quote">
  <svg style="position:absolute;inset:0" width="1200" height="477">
    <polygon points="0,40 260,90 0,70" fill="#0094d4"/>
    <polygon points="1200,20 960,110 1200,60" fill="#0094d4"/>
    <polygon points="0,380 300,360 0,410" fill="#0094d4"/>
    <polygon points="1200,400 900,470 1200,440" fill="#0094d4"/>
    <polygon points="420,477 360,400 440,477" fill="#0094d4"/>
  </svg>
  <h2 class="slab" style="position:absolute;left:0;top:68px;width:1200px;text-align:center;font-size:38px;color:#fff;letter-spacing:4px">Quick quote</h2>
  <p style="position:absolute;left:320px;top:140px;width:560px;text-align:center;font-size:13.5px;line-height:25px;color:#fff">Sed do eiusmod tempor incididunt ut labore et dolore magna aliqua. Ut enim ad minim veniam ammet.</p>
</section>
<div class="field" style="left:258px;top:2995px;width:220px;height:48px">Name</div>
<div class="field" style="left:490px;top:2995px;width:220px;height:48px">Email</div>
<div class="field" style="left:722px;top:2995px;width:222px;height:48px">Phone</div>
<div class="field" style="left:258px;top:3057px;width:686px;height:95px;align-items:flex-start;padding-top:16px">Write your query here...</div>
<div class="abs send">SEND</div>

<!-- testimonials -->
<h2 class="abs h2 slab" style="top:3344px;font-size:38px">What our customer says</h2>
<div class="tcard" style="left:155px;top:3465px">
  <div class="stars">★★★★★</div>
  <p>Integer eu felis quis neque convallis tempor esed ac tortor. <b>Pellentesque sagittis</b>, erat eu feugiat hendrerit, lectus lorem vehicula erat in pulvinar...</p>
  <div class="who">Dana Morris<small>San Francisco, California</small></div>
</div>
<div class="tcard raised" style="left:455px;top:3430px;height:287px;padding-top:30px">
  <div class="stars">★★★★★</div>
  <p style="margin-top:16px">Luctus et ultrices posuere cubilia curae; <b>Nam rutrum lorem</b> nec mauris lobortis, eget sed vulputa <b>libero pharetra</b>. Ut fermentum sollicitudin nisi eu tempus....</p>
  <div class="who" style="bottom:40px">Nina Alvarez<small>Kansas City, Missouri</small></div>
</div>
<div class="tcard" style="left:757px;top:3465px">
  <div class="stars">★★★★★</div>
  <p>Aenean dui magna, finibus ut tempor nec, posuere vitae elit. Morbi euismod, urna nec convallis tempus, velit tellus <b>ultricies arcu auctor finibus</b>...</p>
  <div class="who">Owen Park<small>Arlington, Washington</small></div>
</div>
<div class="tcard" style="left:1063px;top:3420px;height:287px;padding-top:30px">
  <div class="stars">★★★★★</div>
  <p style="margin-top:16px;white-space:nowrap">Aenean mattis id lo<br>Etiam tristique liber<br><b>quam id</b>, maximus<br>vel ornare lorem.</p>
  <div class="who" style="bottom:40px">Dana Morris<small>San Francisco, California</small></div>
</div>
<svg class="abs" style="left:1014px;top:3806px" width="16" height="16" viewBox="0 0 16 16"><path d="M14 8H2M7 3L2 8l5 5" fill="none" stroke="#bbb" stroke-width="1.4"/></svg>
<div class="abs" style="left:1052px;top:3793px;width:44px;height:44px;border-radius:50%;background:var(--blue);box-shadow:0 4px 10px rgba(0,169,221,.4);display:flex;align-items:center;justify-content:center">
  <svg width="16" height="16" viewBox="0 0 16 16"><path d="M2 8h12M9 3l5 5-5 5" fill="none" stroke="#fff" stroke-width="1.6"/></svg>
</div>

<!-- footer -->
<footer class="abs footer"></footer>
<h3 class="abs sub-title slab">Subscribe newsletters</h3>
<div class="abs sub-input">Your email address</div>
<div class="abs sub-btn">SUBMIT</div>
<div class="abs tagline">SIGN UP TO RECIVE OUR LATEST NEWS SIRECTLY IN YOUR MAIL</div>

<div class="abs" style="left:156px;top:4180px;display:flex;align-items:center;gap:8px">
  <i style="width:18px;height:18px;border-radius:50%;background:var(--yellow);display:block"></i>
  <span style="font-family:'Oswald',sans-serif;font-weight:600;font-size:22px;color:var(--blue);line-height:1;text-transform:uppercase">Brightcoat<br>Painting</span>
</div>
<p class="abs" style="left:156px;top:4284px;width:210px;font-size:11px;line-height:19px;color:#8d8d96">Donec sodales sapien at mauris dapib sed luctus nisi interdum sed. Nullam feugiat leo eros, ut aliquam urna lacinia vehicula.</p>

<div class="abs fcol" style="left:456px"><h4>QUICK LINKS</h4>Home<br>About<br>Residential<br>Commercial<br>Before/after videos<br>Contact us</div>
<div class="abs fcol" style="left:648px"><h4>SERVICES</h4>Repair and maintenance<br>Decoration visualization<br>Residential painting<br>Commercial painting</div>
<div class="abs fcol" style="left:883px;line-height:19px"><h4 style="margin-bottom:16px">CONTACT INFO</h4>88 Harbor Lane, Suite 12,<br>Lakeview, 00000
  <div style="display:flex;align-items:center;gap:12px;margin-top:18px"><svg width="14" height="10" viewBox="0 0 14 10"><rect width="14" height="10" fill="#8d8d96"/><path d="M0 0l7 5 7-5" fill="none" stroke="#1d1d23"/></svg>555.010.2040</div>
  <div style="display:flex;align-items:center;gap:12px;margin-top:14px"><svg width="14" height="14" viewBox="0 0 14 14"><path d="M3 1l3 3-2 2a8 8 0 0 0 4 4l2-2 3 3-2 2C6 13 1 8 1 3z" fill="#8d8d96"/></svg>hello@brightcoatpaint.com</div>
</div>

<div class="abs bottombar">
  <span style="position:absolute;left:156px;top:27px">Copyright © 2023 <span style="color:var(--blue)">Brightcoat</span> . All rights reserved</span>
  <span class="soc" style="left:906px"></span>
  <span class="soc" style="left:943px"></span>
  <span class="soc" style="left:980px"></span>
  <span class="soc" style="left:1017px"></span>
</div>

</body>
</html>
```